Bold Modern Creative Wine Label Needed for a Chardonnay

We need a modern, eye catching label, one that will appeal to millennials, but also attract the older more conservative crowd. We like the boldness of black on white but are open to your suggestions. Since the bottle type is a light green 'burgundy style' bottle, you should take that into account. The name of the brand is Vo`. The attached label is example of what we like very much. It is eye catching and bold and modern. Keep in mind that the bottle will be light green in color so black and white might not work so well. Use your creativity please! The label can be any size but needs to fit on this shape bottle. See attached photos. thanks!!

(Please no grapes or wine glasses or wine bottles featured on the label!)
Updates

Hi Designers, I just wanted to let you know that we received many great designs and we are sorting through them this week. The website is making it a bit difficult to create a 'poll' so this is taking longer than we expected. Thanks for all the great submissions!

```html
<!DOCTYPE html>
<html lang="en">
<head>
<meta charset="utf-8">
<title>Vo` Chardonnay Label</title>
<link rel="stylesheet" href="https://fonts.googleapis.com/css2?family=Cormorant+Garamond:wght@400;600&family=Playfair+Display:ital,wght@0,400;1,400&display=swap">
<style>
  :root {
    --backdrop: #ecebe6;
    --paper: #f4f4f2;
    --paper-shade: #e6e6e3;
    --foil: #b9b4a6;
    --ink: #111111;
    --ink-soft: #333333;
  }
  html, body {
    margin: 0;
    padding: 0;
    width: 1200px;
    height: 730px;
    overflow: hidden;
    background: var(--backdrop);
  }
  .canvas {
    position: relative;
    width: 1200px;
    height: 730px;
  }
  .label {
    position: absolute;
    left: 260px;
    top: 25px;
    width: 680px;
    height: 680px;
  }
  .label__shape {
    position: absolute;
    inset: 0;
  }
  .label__brand {
    position: absolute;
    left: 0;
    right: 0;
    top: 200px;
    text-align: center;
    font-family: "Cormorant Garamond", serif;
    font-weight: 600;
    font-size: 170px;
    line-height: 1;
    color: var(--ink);
    letter-spacing: 2px;
  }
  .label__stat {
    position: absolute;
    top: 480px;
    font-family: "Playfair Display", serif;
    color: var(--ink);
    line-height: 1;
  }
  .label__stat--abv { left: 79px; text-align: left; }
  .label__stat--volume { right: 66px; font-size: 34px; }
  .label__abv-value { font-size: 32px; }
  .label__abv-unit {
    display: block;
    font-size: 19px;
    letter-spacing: 4px;
    margin-top: 4px;
  }
  .label__volume-unit { font-style: italic; font-size: 24px; }
  .label__winery {
    position: absolute;
    left: 0; right: 0;
    top: 500px;
    text-align: center;
    font-family: "Cormorant Garamond", serif;
    font-size: 28px;
    letter-spacing: 9px;
    color: var(--ink-soft);
  }
  .label__varietal {
    position: absolute;
    left: 0; right: 0;
    top: 538px;
    text-align: center;
    font-family: "Playfair Display", serif;
    font-size: 36px;
    color: var(--ink-soft);
    transform: scaleX(0.8);
  }
  .label__vintage {
    position: absolute;
    left: 0; right: 0;
    top: 602px;
    text-align: center;
    font-family: "Cormorant Garamond", serif;
    font-size: 18px;
    letter-spacing: 6px;
    color: var(--ink-soft);
  }
</style>
</head>
<body>
<main class="canvas">
  <section class="label" aria-label="Chardonnay wine label">
    <svg class="label__shape" width="680" height="680" viewBox="0 0 680 680" aria-hidden="true">
      <defs>
        <radialGradient id="paper-tone" cx="50%" cy="45%" r="70%">
          <stop offset="0%" stop-color="var(--paper)"/>
          <stop offset="100%" stop-color="var(--paper-shade)"/>
        </radialGradient>
      </defs>
      <polygon points="84,0 596,0 680,84 680,596 596,680 84,680 0,596 0,84" fill="url(#paper-tone)"/>
      <polygon points="155,24 525,24 656,155 656,525 525,656 155,656 24,525 24,155" fill="none" stroke="var(--foil)" stroke-width="2.5"/>
    </svg>
    <div class="label__brand">Vo`</div>
    <div class="label__stat label__stat--abv">
      <span class="label__abv-value">15%</span>
      <span class="label__abv-unit">VOL</span>
    </div>
    <div class="label__winery">Vo’Winery</div>
    <div class="label__stat label__stat--volume">750<span class="label__volume-unit">ml</span></div>
    <div class="label__varietal">Chardonnay</div>
    <div class="label__vintage">-2010-</div>
  </section>
</main>
</body>
</html>
```